Elite boxing brochure

I need a brochure for a boxing training camp please. I would like it to look like the imagery on our Desmond Okafor website http://www.okaforfightcamp.com/ . I have attached some images and the text to be included. The final design needs to attract High net worth individuals, and communicate exclusivity. many thanks. Pete. Please feel free to copy any images from our Okafor website- we have the license to use any and all images on that site

```html
<!DOCTYPE html>
<html lang="en">
<head>
<meta charset="utf-8">
<title>Desmond Okafor Elite Boxing Camp – Agenda</title>
<link href="https://fonts.googleapis.com/css2?family=Roboto+Slab:wght@300;400;700;800&display=swap" rel="stylesheet">
<style>
  :root{
    --paper:#fbf6ec;
    --ink:#2b2b2b;
    --red:#e1373a;
    --band:#e8363a;
    --rule:#7a7a7a;
    --ghost-1:#d9d5cd;
    --ghost-2:#ece7de;
  }
  *{margin:0;padding:0;box-sizing:border-box}
  html,body{width:849px;height:1200px;overflow:hidden;background:var(--paper)}
  body{font-family:"Roboto Slab",Georgia,serif;color:var(--ink);font-weight:300}
  .page{position:relative;width:849px;height:1200px;overflow:hidden;background:var(--paper)}
  .backdrop-portrait{position:absolute;left:110px;top:195px;width:660px;height:860px;
    border-radius:48% 48% 44% 44%;
    background:radial-gradient(ellipse at 50% 45%,var(--ghost-1) 0%,var(--ghost-2) 55%,rgba(251,246,236,0) 75%)}
  .block{position:absolute}
  .label{color:var(--red);font-weight:700;font-size:13.5px}
  .extras{left:65px;top:40px;font-size:14px;line-height:26.3px}
  .extras .label{display:block;margin-bottom:2px}
  .agenda-title{left:64px;top:208px;color:var(--red);font-weight:800;font-size:28px}
  .day{top:273px;font-size:14px;line-height:17.6px}
  .day .label{font-size:14.5px}
  .day b{font-weight:700}
  .day-1{left:65px}
  .day-2{left:308px}
  .day-3{left:598px}
  .gap{margin-top:17.6px}
  .divider{position:absolute;width:1px;background:var(--rule)}
  .divider-a{left:294px;top:252px;height:218px}
  .divider-b{left:579px;top:252px;height:218px}
  .divider-c{left:447px;top:504px;height:298px}
  .list{font-size:14px;line-height:17.6px}
  .workshops{left:65px;top:504px;width:400px}
  .lectures{left:462px;top:504px;width:380px}
  .lectures .row{display:flex}
  .lectures .topic{white-space:pre}
  .lectures .space{margin-top:17.6px}
  .note{left:65px;top:826px;font-size:14px}
  .analysis{left:65px;top:858px;font-size:14px;line-height:17.6px}
  .who{left:65px;top:907px;width:720px;font-size:13.6px;line-height:17.6px}
  .who p{margin-top:14px}
  .footer{position:absolute;left:0;top:1072px;width:849px;height:128px;background:var(--band);
    color:#fff;font-weight:700;text-align:center;font-size:16px}
  .footer .when{position:absolute;top:28px;width:100%;line-height:20px}
  .footer .contact{position:absolute;top:84px;width:100%}
</style>
</head>
<body>
<div class="page">
  <div class="backdrop-portrait" role="img" aria-label="Large faint sepia portrait of the boxer used as a background decoration"></div>

  <div class="block extras">
    <span class="label">In addition we will provide you with</span>
    <div>A Personalised training plan for 6 months</div>
    <div>A personalised action plan to improve technique</div>
    <div>A personalised video showcasing your training to show to your friends and family</div>
    <div>Desmond Okafor Branded Folder for your own notes</div>
    <div>Desmond Okafor Certified plaque</div>
  </div>

  <h1 class="block agenda-title">Agenda</h1>

  <div class="block day day-1">
    <div class="label">Day 1&nbsp; Thursday 16th April</div>
    <div>Introductions</div>
    <div>Technical Workshops</div>
    <div>Explanation Lectures</div>
    <div>Lunch</div>
    <div>Technical Workshops</div>
    <div>Fight Analysis</div>
    <div>Technical Workshops</div>
    <div class="gap"><b>Evening:</b>&nbsp; Watch some of the<br>best fights of all time ,</div>
  </div>
  <div class="divider divider-a"></div>
  <div class="block day day-2">
    <div class="label">Day 2Friday 17th April</div>
    <div>Technical Workshops</div>
    <div>Explanation Lectures</div>
    <div>Lunch</div>
    <div>Technical Workshops</div>
    <div>Fight Analysis</div>
    <div>Technical Workshops</div>
    <div class="gap"><b>Evening:</b>&nbsp; Watch some of the best<br>fights of all time , boxing trivia quiz</div>
  </div>
  <div class="divider divider-b"></div>
  <div class="block day day-3">
    <div class="label">Day 3&nbsp; Saturday 18th April</div>
    <div>Technical Workshops</div>
    <div>Explanation Lectures</div>
    <div>Lunch</div>
    <div>Technical Workshops</div>
    <div>Fight Analysis</div>
    <div>Technical Workshops</div>
    <div class="gap"><b>Evening</b> Depart</div>
  </div>

  <div class="block list workshops">
    <div class="label">Technical Workshops will cover:</div>
    <div>Sparring,</div>
    <div>Technical training</div>
    <div>Correct footwork</div>
    <div>Punching harder workshop</div>
    <div>Balance</div>
    <div>The art of Forcing a stoppage in a fight</div>
    <div>Technical drills-</div>
    <div>Varying the jab to confuse your opponent&nbsp; 4 types</div>
    <div>Points – outscoring your opponent</div>
    <div>Defensive work- the duck slip and swayback</div>
    <div>Combination punching</div>
    <div>Coping strategies for when you are hurt and fatigued</div>
    <div>How to beat a taller / shorter fighter than you</div>
    <div>Power v endurance</div>
    <div>Sustained attacks and counting</div>
    <div>Punch counting</div>
  </div>
  <div class="divider divider-c"></div>
  <div class="block list lectures">
    <div class="label">Explanation Lectures will cover:</div>
    <div class="row"><span class="topic">Physiology: </span><span>The bodys energy systems and how they relate to boxing</span></div>
    <div>Physiology: Measuring progress</div>
    <div>Biomechanics: Punching for power</div>
    <div>Biomechanics: Correct footwork</div>
    <div>Psychology: The inverted U</div>
    <div class="row"><span class="topic">Psychology:  </span><span>Skill acquisition and interference from practice to sparring to competition</span></div>
    <div>Psychology:Visualisation</div>
    <div>Training through injury - training your energy systems not just using boxing</div>
    <div class="space">The 11 things you MUST take to a boxing ring</div>
  </div>

  <div class="block note">(Sparring is optional and will be very carefully controlled.)</div>

  <div class="block analysis">
    <div class="label">Fight analysis</div>
    <div>Review the greatest fights and fighters,</div>
    <div>learn their moves and how you could beat them</div>
  </div>

  <div class="block who">
    <div class="label">Who should come?</div>
    <p>This is an ELITE boxing training camp designed to equip you with knowledge, the skills and a training program to improve massively over a 6 month period. We GUARRANTEE your&nbsp; mprovement if you stick to the program AND eat healthy.&nbsp; You have an opportunity to work with the very best in the world so please be open minded and be prepared to learn. You should come if you want a structured, individualised program of improvement GUARANTEED to work for YOU.</p>
  </div>

  <footer class="footer">
    <div class="when">Date 16-18th April 2015 | Venue ( leave blank)<br>Cost&nbsp;&nbsp; US $ 3000 per person</div>
    <div class="contact">Contact Mr Karim Haddad+971 55 318 4472&nbsp; email:&nbsp; karim@fitcamp-me.com&nbsp; to book</div>
  </footer>
</div>
</body>
</html>
```